Business Card

I need a business card that is fresh, styling and reflects my heart centered healing business while still maintaining full professionalism as I have an my evidence-based practice. I am a Naturopath and a Shiatsu Massage Therapist.
Below are my existing logo (file 1) and an inspiration image (file 2) that reflects the colours and style I would like to express to my card (blues greens). I especially like that tree wallpaper.

Information for the card:
Tessa Gorrinde
BHSc. (Nat) m.QRPC
Naturopath
Herbalist
Nutritionist
Shiatsu Therapist
Wellness Counsellor

41 Dovertan St South Fremantle
www.tessagorrinde.com.au
tessa@tessagorrinde.com.au

NOte: I've removed part of the brief, in that I've changed my mind about the back of the card being a '5 treatments and get sixth one free" I'd rather have this on a separate card. So please do not include this in your designs.
Updates

Hi Guys, I've taken the '5 session get the sixth free' part out of the brief. Also, I've added the info to go on the business card into the brief.

Thanks and happy designing
Tes

I've just uploaded a high res better quality version of the hand logo. Thanks Lovlies. 

Target Market(s)

I am targeting western women of ages 25 - 40 in preconception care, sugar addiction therapy, and wellness coaching. I want must card to be vibrant, positive and current.

Industry/Entity Type

Business

Requirements
Must have
• Please include my hand image logo

```html
<!DOCTYPE html>
<html lang="en">
<head>
<meta charset="utf-8">
<title>Tessa Gorrinde — Business Card</title>
<link rel="stylesheet" href="https://fonts.googleapis.com/css2?family=Cinzel:wght@700;900&family=Crimson+Text&display=swap">
<style>
  :root {
    --page: #ffffff;
    --blush: #f3c9c1;
    --blush-soft: #f6d6cf;
    --leaf: #7fd86a;
    --leaf-deep: #3fb83a;
    --ink: #111111;
    --glow: #ffffff;
    --mark-blue: #2a5bd7;
  }
  html, body {
    margin: 0;
    padding: 0;
    width: 1200px;
    height: 741px;
    overflow: hidden;
    background: var(--page);
  }
  .card {
    position: absolute;
    left: 11px;
    top: 11px;
    width: 1180px;
    height: 718px;
    overflow: hidden;
  }
  .card__wallpaper {
    position: absolute;
    inset: 0;
    background:
      radial-gradient(ellipse at 80% 20%, rgba(127,216,106,0.35), transparent 55%),
      radial-gradient(ellipse at 15% 85%, rgba(127,216,106,0.30), transparent 50%),
      linear-gradient(135deg, var(--blush) 0%, var(--blush-soft) 50%, var(--blush) 100%);
  }
  .card__text {
    position: absolute;
    color: var(--ink);
    text-shadow: 0 0 6px var(--glow), 0 0 12px var(--glow), 0 0 3px var(--glow);
  }
  .name {
    left: 62px;
    top: 52px;
    margin: 0;
    font-family: "Cinzel", serif;
    font-weight: 900;
    font-size: 72px;
    line-height: 1;
    letter-spacing: 1px;
  }
  .services {
    left: 62px;
    top: 146px;
    margin: 0;
    padding: 0;
    list-style: none;
    font-family: "Cinzel", serif;
    font-weight: 900;
    font-size: 43px;
    line-height: 58.5px;
  }
  .contact {
    left: 452px;
    top: 522px;
    margin: 0;
    font-family: "Crimson Text", serif;
    font-style: normal;
    font-size: 42px;
    line-height: 61px;
  }
  .brand-mark {
    position: absolute;
    left: 745px;
    top: 200px;
    display: flex;
    align-items: center;
    gap: 10px;
    font-family: "Cinzel", serif;
    font-weight: 700;
    font-size: 26px;
    color: var(--mark-blue);
  }
  .brand-mark__dot {
    width: 30px;
    height: 30px;
    border-radius: 50%;
    background: var(--mark-blue);
  }
</style>
</head>
<body>
  <main class="card">
    <div class="card__wallpaper" role="img" aria-label="Repeating wallpaper of green palm and round-canopy trees on a blush pink ground"></div>

    <h1 class="card__text name">Tessa Gorrinde</h1>

    <ul class="card__text services">
      <li>BHSc. (Nat) m.QRPC</li>
      <li>Naturopath</li>
      <li>Herbalist</li>
      <li>Nutritionist</li>
      <li>Shiatsu Therapist</li>
      <li>Wellness Counsellor</li>
    </ul>

    <div class="brand-mark">
      <span class="brand-mark__dot"></span>
      <span>Tes</span>
    </div>

    <address class="card__text contact">
      41 Dovertan St South Fremantle<br>
      www.tessagorrinde.com.au<br>
      tessa@tessagorrinde.com.au
    </address>
  </main>
</body>
</html>
```